Marketing Expert Needs a Book Cover Design to Inspire Audiences

Need a book cover design for my first book!
The book is a ‘How To’ serious non fiction book. It has insights for marketers on how to transform their marketing to help their organizations accelerate sales and drive growth. This is not a high level theoretical book about brand building. Instead this includes strategic frameworks, and tried and tested ideas and tactics which marketers (or aspiring marketers) can use to be successful in their jobs. The premise of this book is that it’s no longer enough for marketers to focus on brand recognition. We need to help the business to create demand and make it easier for our sales colleagues to close deals.
The aim is to inspire readers with insights so that they think differently about themselves and their marketing. The aim is to compel them to take start new conversations to accelerate sales, using the tools, concepts and case studies outlined in the book.
The Title: The Growth Signal
Subtitle: Steps to Win Buyers by Storytelling, Curiosity and Trusted Voices.
The cover must have a compelling visual which communicates this idea-
The Growth Signal Inspires You to Think Different so That You Scale/Overcome the Limits you might have placed on yourself or your business.
I like a simple and clean look. I'm attaching some samples which I like. Looking to achieve the same look for my book cover.
Update- I need the cover for an ebook only. Since the cover will be displayed as a thumbnail in Verbolt and other online shopping sites, it should be without any clutter with good contrast between images and text. This will help with visibility.
Updates
Key Art Style designs will also be welcome. Added Saturday, September 24, 2016
Reason: I'm hoping that atleast some more top 20 designers will respond.
Target Market(s)
Target market is CMOs, Marketing Managers, Business Leaders, MBA students- anyone who is looking to reshape and rejig their marketing skills and teams.
Industry/Entity Type
Marketing
Requirements
Must have
- A compelling visual is a must have.
- It shouldn't have only text.
Nice to have
- Please refer the cover samples I sent.
- Key Art designs will also be welcome.
Should not have
- Clutter.
- I like simplicity.

```html
<!DOCTYPE html>
<html lang="en">
<head>
<meta charset="utf-8">
<title>The Growth Signal — Ebook Cover</title>
<link rel="stylesheet" href="https://fonts.googleapis.com/css2?family=Bebas+Neue&display=swap">
<style>
  :root {
    --page-bg: #ececec;
    --cover-light: #fff7b0;
    --cover-mid: #ffe94a;
    --cover-deep: #f6c81c;
    --photo-amber: #e39a1c;
    --photo-rust: #b9641a;
    --photo-haze: #f3cf3a;
    --ink-dark: #2c2410;
    --ink-red: #8e2a12;
    --ink-sub: #4a1606;
  }
  * { margin: 0; padding: 0; box-sizing: border-box; }
  html, body {
    width: 1200px;
    height: 900px;
    overflow: hidden;
    background: var(--page-bg);
  }
  .stage {
    position: relative;
    width: 1200px;
    height: 900px;
  }
  .cover {
    position: absolute;
    left: 360px;
    top: 66px;
    width: 480px;
    height: 768px;
    overflow: hidden;
    font-family: "Bebas Neue", "Oswald", sans-serif;
    background: linear-gradient(180deg, var(--cover-light) 0%, var(--cover-mid) 32%, var(--cover-deep) 100%);
    box-shadow: 0 8px 30px rgba(0,0,0,0.12);
  }
  .cover-photo {
    position: absolute;
    left: 0;
    top: 210px;
    width: 480px;
    height: 558px;
    background:
      radial-gradient(ellipse 34% 28% at 70% 20%, var(--photo-rust) 0%, rgba(185,100,26,0.6) 45%, transparent 100%),
      radial-gradient(ellipse 45% 60% at 72% 62%, var(--photo-amber) 0%, rgba(227,154,28,0.75) 50%, transparent 100%),
      linear-gradient(180deg, transparent 0%, var(--photo-haze) 22%, var(--photo-haze) 100%);
    -webkit-mask-image: linear-gradient(180deg, transparent 0%, #000 18%, #000 100%);
    mask-image: linear-gradient(180deg, transparent 0%, #000 18%, #000 100%);
  }
  .cover-title {
    position: absolute;
    left: 41px;
    top: 44px;
    font-size: 80px;
    line-height: 74px;
    letter-spacing: 2px;
    font-weight: 400;
    background: linear-gradient(90deg, var(--ink-dark) 0%, var(--ink-dark) 35%, var(--ink-red) 100%);
    -webkit-background-clip: text;
    background-clip: text;
    color: transparent;
  }
  .cover-subtitle {
    position: absolute;
    left: 41px;
    top: 520px;
    color: var(--ink-sub);
  }
  .subtitle-lead {
    display: block;
    font-size: 15px;
    line-height: 18px;
    letter-spacing: 9px;
    margin-bottom: 2px;
  }
  .subtitle-key {
    display: block;
    font-size: 38px;
    line-height: 39px;
    letter-spacing: 1px;
  }
  .subtitle-key--spaced { margin-bottom: 8px; }
</style>
</head>
<body>
  <main class="stage">
    <article class="cover">
      <div class="cover-photo" role="img" aria-label="Yellow-toned photograph of a man in a suit jacket looking into the distance beside a car"></div>
      <h1 class="cover-title">The Growth<br>Signal</h1>
      <p class="cover-subtitle">
        <span class="subtitle-lead">Steps to</span>
        <span class="subtitle-key subtitle-key--spaced">Win Buyers</span>
        <span class="subtitle-lead">By</span>
        <span class="subtitle-key">Storytelling</span>
        <span class="subtitle-key">Curiosity</span>
        <span class="subtitle-key">Trusted Voices</span>
      </p>
    </article>
  </main>
</body>
</html>
```